I need the Scorecard I've developed for my staff to be produced into a visually engaging piece that will encourage the staff to utilize it on a daily basis. I'm thinking it could be 5x7 in size so that it isn't too cumbersome, but I'm open to different layouts.
I have multiple other departments that will need Scorecards created for them as well, but each one will contain task specific questions for each department.

```html
<!DOCTYPE html>
<html lang="en">
<head>
<meta charset="utf-8">
<title>Receptionist Daily Excellence Scorecard</title>
<link rel="stylesheet" href="https://fonts.googleapis.com/css2?family=Libre+Baskerville:wght@400;700&family=Arimo:wght@400;700&display=swap">
<style>
  :root {
    --brand-blue: #1b6db6;
    --band-blue: #dde9f6;
    --accent-orange: #f0672e;
    --ink: #1d1d1d;
    --rule: #b9b9b9;
    --page-bg: #ece9e4;
    --card-bg: #ffffff;
    --footer-rule: #5b97cf;
    --serif: "Libre Baskerville", Georgia, serif;
    --sans: "Arimo", Arial, sans-serif;
  }
  * { box-sizing: border-box; margin: 0; padding: 0; }
  html, body { width: 918px; height: 1200px; overflow: hidden; background: var(--page-bg); }
  .scorecard {
    position: absolute; left: 76px; top: 63px;
    width: 750px; height: 1050px;
    background: var(--card-bg);
    transform: scale(1.0223); transform-origin: 0 0;
    color: var(--ink);
    box-shadow: 0 2px 10px rgba(0,0,0,.15);
  }
  .abs { position: absolute; }
  .title-band { left: 0; top: 0; width: 750px; height: 64px; background: var(--brand-blue); }
  .title-band h1 { position: absolute; left: 27px; top: 12px; font: 400 31px/1.2 var(--serif); color: #fff; letter-spacing: .1px; }
  .title-rule { left: 0; top: 66px; width: 750px; height: 2px; background: var(--accent-orange); }
  .title-icon { right: 22px; top: 7px; }

  .meta-row { top: 93px; font: 400 17px var(--serif); }
  .line { position: absolute; height: 1px; background: var(--rule); }

  .section-bar { left: 0; width: 750px; height: 42px; background: var(--band-blue); }
  .section-bar h2 { position: absolute; left: 27px; top: 9px; font: 400 21px/1.2 var(--serif); }
  .section-bar h2 small { font-size: 15px; }
  .section-bar svg { position: absolute; }

  .scale-key { top: 188px; font: 400 15.5px var(--serif); color: var(--accent-orange); }
  .col-head { top: 289px; font: 400 15.5px var(--serif); color: var(--accent-orange); }
  .task { left: 26px; font: 400 14.5px var(--sans); }

  .status { font: 400 14.5px var(--sans); color: var(--accent-orange); }
  .status-desc { font: 400 12.5px/1.35 var(--sans); }
  .radio { position: absolute; width: 12px; height: 12px; border: 1.3px solid var(--ink); border-radius: 50%; }
  .prompt { font: 400 12.5px var(--sans); color: var(--accent-orange); }

  .overall { left: 24px; top: 884px; font: 400 21px var(--serif); }
  .overall-sub { left: 24px; top: 914px; font: 400 10.5px var(--serif); }

  .footer-band { left: 0; top: 955px; width: 750px; height: 95px; background: var(--brand-blue); }
  .sign-label { top: 976px; font: 700 13.5px var(--sans); color: #fff; }
  .footer-rule { position: absolute; height: 1px; background: var(--footer-rule); top: 1025px; }
  .footer-icon { left: 675px; top: 962px; opacity: .35; }
</style>
</head>
<body>
<main class="scorecard">
  <header class="abs title-band">
    <h1>Receptionist Daily Excellence Scorecard</h1>
    <svg class="abs title-icon" width="36" height="50" viewBox="0 0 36 50" fill="none" stroke="#fff" stroke-width="2">
      <rect x="9" y="3" width="24" height="32"/>
      <line x1="14" y1="11" x2="28" y2="11"/><line x1="14" y1="17" x2="28" y2="17"/><line x1="14" y1="23" x2="28" y2="23"/>
      <path d="M4 30v14h10l6-8-6-2V26"/>
    </svg>
  </header>
  <div class="abs title-rule"></div>

  <div class="abs meta-row" style="left:26px">Name:</div>
  <div class="line" style="left:89px;width:165px;top:110px"></div>
  <div class="abs meta-row" style="left:271px">Date:</div>
  <div class="line" style="left:321px;width:166px;top:110px"></div>
  <div class="abs meta-row" style="left:504px">Location:</div>
  <div class="line" style="left:590px;width:156px;top:110px"></div>

  <section class="abs section-bar" style="top:135px">
    <h2>Please Rate Yourself For Each Task</h2>
    <svg style="left:646px;top:7px" width="84" height="28" viewBox="0 0 84 28" fill="none" stroke="var(--ink)" stroke-width="1.4">
      <path d="M8 14l2 4 4 .5-3 3 .8 4-3.8-2-3.8 2 .8-4-3-3 4-.5z"/>
      <path d="M24 10l2 4.5 4.5.5-3.3 3 .9 4.5-4.1-2.3-4.1 2.3.9-4.5-3.3-3 4.5-.5z"/>
      <path d="M42 3l2.6 5.6 6 .7-4.5 4.1 1.2 6-5.3-3-5.3 3 1.2-6-4.5-4.1 6-.7z"/>
      <path d="M60 10l2 4.5 4.5.5-3.3 3 .9 4.5-4.1-2.3-4.1 2.3.9-4.5-3.3-3 4.5-.5z"/>
      <path d="M76 14l2 4 4 .5-3 3 .8 4-3.8-2-3.8 2 .8-4-3-3 4-.5z"/>
    </svg>
  </section>
  <div class="abs scale-key" style="left:26px">1 = Needs Improvement</div>
  <div class="abs scale-key" style="left:297px">3 = Meets Expectations</div>
  <div class="abs scale-key" style="left:603px">5 = Excellent</div>

  <section class="abs section-bar" style="top:237px">
    <h2>Call Handling &amp; First Call Intake</h2>
    <svg style="left:650px;top:3px" width="36" height="36" viewBox="0 0 36 36" fill="none" stroke="var(--ink)" stroke-width="1.8">
      <circle cx="16" cy="13" r="7"/>
      <path d="M7 13a9 9 0 0 1 18 0M7 12v4M25 12v4M25 16c0 3-3 4-6 4"/>
      <path d="M3 34c0-7 6-11 13-11s9 2 11 4"/>
      <circle cx="28" cy="28" r="5"/><path d="M25.5 28l2 2 3-3.5"/>
    </svg>
    <svg style="left:697px;top:4px" width="34" height="34" viewBox="0 0 34 34" fill="none" stroke="var(--ink)" stroke-width="2">
      <path d="M6 3l6 0 3 7-4 3c2 4 5 7 9 9l3-4 7 3v6c0 2-2 3-4 3C15 29 3 17 3 6c0-2 1-3 3-3z"/>
      <path d="M31 3L19 15M19 7v8h8"/>
    </svg>
  </section>
  <div class="abs col-head" style="left:26px">Task</div>
  <div class="abs col-head" style="left:423px">Self-Rating (1-5)</div>
  <div class="abs col-head" style="left:575px">Notes / Issues</div>

  <div class="abs task" style="top:321px">Answered 90%+ calls within 3 rings</div>
  <div class="abs task" style="top:354px">Maintained empathy and professionalism</div>
  <div class="abs task" style="top:386px">Accurately completed all First Call fields</div>
  <div class="abs task" style="top:419px">Worked within Receptionist role</div>
  <div class="line" style="left:416px;width:135px;top:335px"></div>
  <div class="line" style="left:560px;width:134px;top:335px"></div>
  <div class="line" style="left:416px;width:135px;top:367px"></div>
  <div class="line" style="left:560px;width:134px;top:367px"></div>
  <div class="line" style="left:416px;width:135px;top:400px"></div>
  <div class="line" style="left:560px;width:134px;top:400px"></div>
  <div class="line" style="left:416px;width:135px;top:432px"></div>
  <div class="line" style="left:560px;width:134px;top:432px"></div>

  <section class="abs section-bar" style="top:460px">
    <h2>Daily Status Summary <small>(Circle One)</small></h2>
    <svg style="left:704px;top:6px" width="30" height="32" viewBox="0 0 30 32" fill="none" stroke="var(--ink)" stroke-width="1.6">
      <rect x="2" y="22" width="4" height="7"/><rect x="9" y="18" width="4" height="11"/><rect x="16" y="14" width="4" height="15"/><rect x="23" y="10" width="4" height="19"/>
      <line x1="0" y1="31" x2="30" y2="31"/><path d="M2 14L24 2M19 2h5v5"/>
    </svg>
  </section>
  <span class="radio" style="left:39px;top:522px"></span>
  <div class="abs status" style="left:64px;top:519px">Excellent</div>
  <div class="abs status-desc" style="left:64px;top:541px">All key duties completed,<br>proactive, calm under<br>pressure</div>
  <span class="radio" style="left:256px;top:522px"></span>
  <div class="abs status" style="left:281px;top:519px">Satisfactory</div>
  <div class="abs status-desc" style="left:281px;top:541px">Most duties completed,<br>minor follow-up needed</div>
  <span class="radio" style="left:503px;top:522px"></span>
  <div class="abs status" style="left:528px;top:519px">Needs Support</div>
  <div class="abs status-desc" style="left:528px;top:541px">Missed urgent duties,<br>accuracy or stress issues</div>

  <section class="abs section-bar" style="top:615px">
    <h2 style="left:32px">Daily Reflection</h2>
    <svg style="left:678px;top:4px" width="54" height="34" viewBox="0 0 54 34" fill="none" stroke="var(--ink)" stroke-width="1.8">
      <path d="M3 30a24 24 0 0 1 48 0"/><path d="M10 30a17 17 0 0 1 34 0"/>
      <path d="M8 19l6 3M16 10l4 5M27 6v6M38 10l-4 5M46 19l-6 3"/>
      <circle cx="27" cy="24" r="7"/><circle cx="27" cy="22" r="2"/><path d="M23 29c1-3 7-3 8 0"/>
    </svg>
  </section>
  <span class="radio" style="left:27px;top:679px"></span>
  <div class="abs prompt" style="left:45px;top:679px">What went well today?</div>
  <span class="radio" style="left:244px;top:679px"></span>
  <div class="abs prompt" style="left:265px;top:679px">Any issues or barriers to note?</div>
  <span class="radio" style="left:492px;top:679px"></span>
  <div class="abs prompt" style="left:510px;top:679px">Support needed from supervisor?</div>
  <div class="line" style="left:45px;width:135px;top:710px"></div>
  <div class="line" style="left:45px;width:135px;top:732px"></div>
  <div class="line" style="left:265px;width:181px;top:710px"></div>
  <div class="line" style="left:265px;width:181px;top:732px"></div>
  <div class="line" style="left:510px;width:201px;top:710px"></div>
  <div class="line" style="left:510px;width:201px;top:732px"></div>

  <section class="abs section-bar" style="top:754px">
    <h2>Stars &amp; Flags <small>(Supervisor Use Only)</small></h2>
    <svg style="left:661px;top:3px" width="34" height="34" viewBox="0 0 34 34" fill="none" stroke="var(--ink)" stroke-width="2">
      <path d="M17 2l4.3 9.3 10 1.2-7.4 6.9 2 10-8.9-5-8.9 5 2-10-7.4-6.9 10-1.2z"/>
    </svg>
    <svg style="left:702px;top:3px" width="30" height="36" viewBox="0 0 30 36" fill="none" stroke="var(--ink)" stroke-width="2">
      <path d="M4 2v32M4 4h22l-5 7 5 7H4"/>
    </svg>
  </section>
  <span class="radio" style="left:27px;top:814px"></span>
  <div class="abs prompt" style="left:45px;top:814px">Stars (Excellence or above-and-beyond moments):</div>
  <span class="radio" style="left:381px;top:815px"></span>
  <div class="abs prompt" style="left:405px;top:815px">Flags (Concerns needing follow-up/coaching)</div>
  <div class="line" style="left:45px;width:305px;top:844px"></div>
  <div class="line" style="left:45px;width:305px;top:866px"></div>
  <div class="line" style="left:405px;width:305px;top:845px"></div>
  <div class="line" style="left:405px;width:305px;top:867px"></div>

  <div class="abs overall">Manager's Overall Rating</div>
  <div class="abs overall-sub">Performance On A 1-5 Scale</div>
  <div class="line" style="left:306px;width:210px;top:913px"></div>

  <footer class="abs footer-band"></footer>
  <div class="abs sign-label" style="left:26px">Receptionist Signature</div>
  <div class="abs sign-label" style="left:241px">Supervisor Signature</div>
  <div class="abs sign-label" style="left:486px">Date</div>
  <div class="footer-rule" style="left:26px;width:161px"></div>
  <div class="footer-rule" style="left:241px;width:150px"></div>
  <div class="footer-rule" style="left:486px;width:190px"></div>
  <svg class="abs footer-icon" width="60" height="84" viewBox="0 0 36 50" fill="none" stroke="#fff" stroke-width="1.5">
    <rect x="9" y="3" width="24" height="32"/>
    <line x1="14" y1="11" x2="28" y2="11"/><line x1="14" y1="17" x2="28" y2="17"/><line x1="14" y1="23" x2="28" y2="23"/>
    <path d="M4 30v14h10l6-8-6-2V26"/>
  </svg>
</main>
</body>
</html>
```